Web Design Project

We are looking for a web page (home) page design for a website that offers Virtual Internet Marketing services.

The Company is called Brindle Marketing, the services we provide are as follows:

Web Design
Social Media Management
SEO/PPC Traffic
Display
Mobile Apps
On & Offline Marketing Services

We see so many web marketing companies that struggle to produce their own great designs and call to actions. 99% of web companies do not understand marketing, so how can they help their customers drive traffic and produce sales!

We require a design that is professional yet fresh and funky! Our goal with the home page is to help prospects understand that our core business is to help them succeed and make more money, by utilising our on and offline marketing experience. We also offer done for you solutions which include - websites, design, traffic, email campaigns etc.

Included should be obvious call to actions to view our services and get our free guide/video

- A clear value proposition that identifies target audience (those that are struggling to make the web work for them)

- Easy to use navigation

We need to include an optin form where we exchange a free training guide or video series in return for an email address, above the fold to the right of the page!

We like the following to provide you with ideas:

http://www.plankorbit.com/
http://www.morvane.co.uk/
http://www.gristlepond.com/
http://www.tarnby.co.uk/ (quite like but too jumbled - too much going on)

Colours are optional, however fresh, vibrant and professional looking.

The final design should be easy on the eye, not lead to any confusion as to what we do and be simple to navigate.

Industry/Entity Type

Marketing

Requirements
Must have
• Optin form
Footer section
showcase of services offered.

```html
<!DOCTYPE html>
<html lang="en">
<head>
<meta charset="utf-8">
<title>Brindle Marketing</title>
<link rel="stylesheet" href="https://fonts.googleapis.com/css2?family=Open+Sans:wght@400;600;700;800&display=swap">
<style>
:root{
  --navy:#0f4a7e;
  --navy-dark:#0a355d;
  --blue:#1f5fa6;
  --orange:#f07a12;
  --orange-dark:#d9620a;
  --green:#8dbf2e;
  --green-light:#a6cf45;
  --grey-band:#ececec;
  --grey-section:#e9e8e8;
  --text:#1b1b1b;
  --footer:#000;
  --footer-text:#fff;
}
*{box-sizing:border-box;margin:0;padding:0}
html,body{width:1200px;height:2186px;overflow:hidden}
body{position:relative;font-family:"Open Sans",Arial,sans-serif;color:var(--text);background:#fff}
.abs{position:absolute}

/* header */
.site-header{left:0;top:0;width:1200px;height:127px;background:linear-gradient(#14578f,var(--navy-dark));border-bottom:10px solid var(--orange)}
.logo{left:53px;top:22px;color:#fff;font-weight:700;font-size:37px;line-height:38px;letter-spacing:-1px}
.social-dots{right:40px;top:32px;display:flex;gap:6px}
.social-dots span{width:27px;height:27px;border-radius:50%;background:#2a86d0}
.social-dots span:last-child{background:#d9452f}
.main-nav{right:44px;top:78px;display:flex;gap:14px;color:#fff;font-size:17px;font-weight:700}
.main-nav .sep{color:var(--green-light)}

/* hero */
.hero{left:0;top:127px;width:1200px;height:433px;background:radial-gradient(ellipse at 40% 40%,var(--green-light),var(--green) 70%)}
.hero-title{left:56px;top:110px;color:var(--navy);font-size:54px;font-weight:800;letter-spacing:1px}
.hero-sub{left:56px;top:180px;color:#fff;font-size:29px;font-weight:800;line-height:36px;text-transform:uppercase}
.btn-quote{left:56px;top:281px;width:352px;height:54px;background:linear-gradient(#2f7bd0,#1552a0);border-radius:4px;color:#fff;font-size:24px;font-weight:700;display:flex;align-items:center;justify-content:center}
.slider-dots{left:56px;top:370px;display:flex;gap:8px}
.slider-dots span{width:20px;height:20px;border-radius:50%;background:#6d9a1f}
.slider-dots span.active{background:var(--navy)}
.hero-art{left:640px;top:30px;width:520px;height:400px}

/* opt-in */
.optin{left:830px;top:236px;width:320px;background:rgba(255,255,255,.95);border-radius:6px;padding:14px 16px;box-shadow:0 2px 8px rgba(0,0,0,.15)}
.optin h3{color:var(--navy);font-size:17px;font-weight:800;line-height:20px}
.optin p{font-size:13px;line-height:17px;margin:4px 0 8px}
.optin-row{display:flex;gap:6px}
.optin-email{flex:1;height:34px;border:1px solid #ccc;color:#888;font-size:14px;padding:7px 10px;background:#fff}
.optin-btn{width:96px;height:34px;background:var(--orange);color:#fff;font-weight:700;font-size:14px;display:flex;align-items:center;justify-content:center;border-radius:3px}

/* proposition band */
.proof-band{left:0;top:560px;width:1200px;height:157px;background:linear-gradient(#f7f7f7,var(--grey-band))}
.proof-text{left:120px;top:43px;width:630px;text-align:center;font-size:30px;font-weight:700;line-height:33px}
.btn-start{left:765px;top:45px;width:232px;height:58px;background:linear-gradient(#f7931e,var(--orange-dark));border-radius:4px;color:#fff;font-size:25px;font-weight:700;display:flex;align-items:center;justify-content:center}

/* services */
.services{left:0;top:717px;width:1200px;height:753px;background:linear-gradient(#fff,#f3f3f3)}
.section-title{left:0;top:18px;width:1200px;text-align:center;color:var(--orange);font-size:29px;font-weight:800}
.card{width:355px;background:#fff;box-shadow:0 1px 4px rgba(0,0,0,.08);padding:70px 20px 0 20px}
.card h3{color:var(--orange);font-size:19px;font-weight:700;margin-bottom:4px;white-space:nowrap}
.card p{font-size:15px;line-height:19px;color:var(--text)}
.card .more{display:block;margin-top:6px;color:var(--navy);font-size:13px;font-weight:800}
.icon-badge{width:104px;height:104px;border-radius:50%;background:var(--blue);display:flex;align-items:center;justify-content:center}

/* testimonial */
.testimonial{left:0;top:1470px;width:1200px;height:224px;background:var(--grey-section)}
.testimonial h2{left:53px;top:30px;color:var(--orange);font-size:23px;font-weight:800}
.client-mark{left:53px;top:88px;display:flex;align-items:center;gap:12px;color:var(--navy);font-size:34px;font-weight:800}
.client-mark span{width:64px;height:64px;border-radius:50%;background:var(--blue)}
.quote{left:311px;top:96px;width:850px;font-size:16px;line-height:20px}
.quote cite{display:block;font-weight:700;font-style:italic}
.pointer{left:334px;top:1694px;width:0;height:0;border-left:14px solid transparent;border-right:14px solid transparent;border-top:14px solid var(--grey-section)}

/* clients */
.client-strip{left:0;top:1694px;width:1200px;height:116px;display:flex;align-items:center;justify-content:space-around;padding:0 30px;color:var(--navy);font-size:27px;font-weight:800}

/* footer */
.footer-accent{left:0;top:1800px;width:1200px;height:42px}
.site-footer{left:0;top:1840px;width:1200px;height:346px;background:var(--footer);color:var(--footer-text)}
.f-col{top:50px}
.f-col h4{font-size:18px;font-weight:600;letter-spacing:1px;color:#aaa;margin-bottom:12px}
.f-col li{list-style:none;font-size:14.5px;line-height:29px}
.f-col .soc{display:flex;align-items:center;gap:8px}
.f-col .soc i{width:17px;height:17px;border-radius:50%;background:#2a86d0;display:inline-block}
.quick h4{left:685px;top:33px;font-size:25px;font-weight:600;letter-spacing:1px}
.field{background:#fff;color:#888;font-size:15px;padding:6px 10px;border:1px solid #ccc}
.btn-send{left:1081px;top:172px;width:64px;height:70px;background:var(--orange);color:#fff;font-weight:700;font-size:16px;display:flex;align-items:center;justify-content:center}
.req-note{left:685px;top:255px;font-size:13px;color:#bbb}
.footer-base{left:53px;top:290px;width:1094px;border-top:1px solid #444;padding-top:14px;display:flex;justify-content:space-between;font-size:14px}
</style>
</head>
<body>

<header class="site-header abs">
  <div class="logo abs">Brindle<br>Marketing</div>
  <div class="social-dots abs"><span></span><span></span><span></span><span></span></div>
  <nav class="main-nav abs">
    <span>Home</span><span class="sep">/</span><span>Who we are</span><span class="sep">/</span><span>What we do</span><span class="sep">/</span><span>Careers</span><span class="sep">/</span><span>Clients</span><span class="sep">/</span><span>Contact</span>
  </nav>
</header>

<section class="hero abs">
  <h1 class="hero-title abs">SOCIAL MEDIA</h1>
  <p class="hero-sub abs">Leave it to us to add a<br>touch of magic to</p>
  <div class="btn-quote abs">REQUEST A FREE QUOTE</div>
  <div class="slider-dots abs"><span></span><span></span><span class="active"></span></div>
  <svg class="hero-art abs" viewBox="0 0 520 400" role="img" aria-label="Illustration of speech bubbles filled with social media icons">
    <defs><linearGradient id="bubbleTone" x1="0" y1="0" x2="1" y2="1"><stop offset="0" stop-color="#f4f8ea"/><stop offset="1" stop-color="#f08a2a"/></linearGradient></defs>
    <rect x="0" y="0" width="520" height="400" rx="40" fill="url(#bubbleTone)" opacity=".85"/>
  </svg>
  <form class="optin abs">
    <h3>Get our free marketing guide</h3>
    <p>Video series and tips to make the web work for you.</p>
    <div class="optin-row"><div class="optin-email">Your email*</div><div class="optin-btn">SEND ME IT</div></div>
  </form>
</section>

<section class="proof-band abs">
  <p class="proof-text abs">90% of consumers trust peer<br>Recommendations from social networks</p>
  <div class="btn-start abs">GET STARTED</div>
</section>

<section class="services abs">
  <h2 class="section-title abs">HERE'S WHAT WE CAN DO FOR YOU</h2>

  <article class="card abs" style="left:53px;top:153px;height:224px"><h3>Web Design</h3><p>Lorem ipsuisthm dolorlor sitamet, consec istetur adiploreis cing eisilt. Aenean vitae magna etta cuipsu feugiat saisgittios mor biidna sit amet, consec isteturisilt.</p><span class="more">+READ MORE</span></article>
  <article class="card abs" style="left:425px;top:153px;height:224px"><h3>Social Media Management</h3><p>Lorem ipsuisthm dolorlor sitamet, consec istetur adiploreis cing eisilt. Aenean vitae magna etta cuipsu feugiat saisgittios mor biidna sit amet, consec isteturisilt.</p><span class="more">+READ MORE</span></article>
  <article class="card abs" style="left:797px;top:153px;height:224px"><h3>SEO/PPC Traffic</h3><p>Lorem ipsuisthm dolorlor sitamet, consec istetur adiploreis cing eisilt. Aenean vitae magna etta cuipsu feugiat saisgittios mor biidna sit amet, consec isteturisilt.</p><span class="more">+READ MORE</span></article>

  <article class="card abs" style="left:53px;top:449px;height:243px"><h3>Display</h3><p>Lorem ipsum dolorlor sitamet, consec istetur adipis cing eisilt. Aenean vitae magna ettacus feugiat saisgittios mor biidna sit amet, consec isteturisilt.</p><span class="more">+READ MORE</span></article>
  <article class="card abs" style="left:425px;top:449px;height:243px"><h3>Mobile Apps</h3><p>Lorem ipsum dolorlor sitamet, consec istetur adipis cing eisilt. Aenean vitae magna ettacus feugiat saisgittios mor biidna sit amet, consec isteturisilt.</p><span class="more">+READ MORE</span></article>
  <article class="card abs" style="left:797px;top:449px;height:243px"><h3>On &amp; Offline Marketing Services</h3><p>Lorem ipsum dolorlor sitamet, consec istetur adipis cing eisilt. Aenean vitae magna ettacus feugiat saisgittios mor biidna sit amet, consec isteturisilt.</p><span class="more">+READ MORE</span></article>

  <div class="icon-badge abs" style="left:178px;top:94px"><svg width="54" height="48" viewBox="0 0 54 48" fill="none" stroke="#fff" stroke-width="4"><rect x="3" y="3" width="48" height="32" rx="2"/><path d="M20 46h14M27 35v11M18 14l8 8M26 14l-8 8"/></svg></div>
  <div class="icon-badge abs" style="left:550px;top:94px"><svg width="54" height="48" viewBox="0 0 54 48" fill="#fff"><rect x="4" y="6" width="30" height="22" rx="3"/><path d="M10 28l-2 8 9-8z"/><rect x="22" y="18" width="28" height="20" rx="3" fill="none" stroke="#fff" stroke-width="3"/></svg></div>
  <div class="icon-badge abs" style="left:922px;top:94px"><svg width="54" height="48" viewBox="0 0 54 48" fill="none" stroke="#fff" stroke-width="4"><rect x="3" y="6" width="48" height="36" rx="2"/><path d="M10 34l11-11 8 7 14-15"/></svg></div>
  <div class="icon-badge abs" style="left:178px;top:404px"><svg width="54" height="54" viewBox="0 0 54 54" fill="#fff"><rect x="24" y="6" width="6" height="46"/><path d="M6 12h36l8 7-8 7H6z"/></svg></div>
  <div class="icon-badge abs" style="left:550px;top:404px"><svg width="40" height="58" viewBox="0 0 40 58" fill="none" stroke="#fff" stroke-width="4"><rect x="4" y="3" width="32" height="52" rx="5"/><path d="M16 47h8"/></svg></div>
  <div class="icon-badge abs" style="left:922px;top:404px"><svg width="58" height="54" viewBox="0 0 58 54" fill="#fff"><circle cx="22" cy="24" r="14"/><g stroke="#fff" stroke-width="6"><path d="M22 4v40M2 24h40M8 10l28 28M36 10L8 38"/></g><circle cx="22" cy="24" r="5" fill="#1f5fa6"/><circle cx="46" cy="42" r="8"/><circle cx="46" cy="42" r="3" fill="#1f5fa6"/></svg></div>
</section>

<section class="testimonial abs">
  <h2 class="abs">HAPPY CLIENTS ARE SAYING</h2>
  <div class="client-mark abs"><span></span>Quellon</div>
  <blockquote class="quote abs">Lorem ipsum dolor sit amet, consectetur adipiscing elit. Donec enim magna, molestie at semper porttitor, varius vitae mi. Vivamus sapien nibh, aliquet eu imperdiet vitae, adipiscing non diam. Quisque sed turpis quam. Sed nec erat magna, in adipiscing varius vitae mivamus sapien nibh alique.<cite>Jane Arden, Social Media Manager, Quellon Global</cite></blockquote>
</section>

<div class="client-strip abs">
  <span>Varnex</span><span>Quellon</span><span>Bramwell Bakes</span><span>Strideline</span><span>Harvale</span><span>Corvik</span>
</div>
<div class="pointer abs"></div>

<svg class="footer-accent abs" viewBox="0 0 1200 42" preserveAspectRatio="none" aria-hidden="true">
  <polygon points="0,42 1200,10 1200,42" fill="#1f5fa6"/>
  <polygon points="0,40 1200,0 1200,24 0,42" fill="#8dbf2e"/>
</svg>

<footer class="site-footer abs">
  <div class="f-col abs" style="left:53px"><h4>WHO WE ARE</h4><ul><li>About</li><li>Features</li><li>Our Team</li><li>Customers</li><li>Affiliate Program</li><li>Social Blog</li></ul></div>
  <div class="f-col abs" style="left:245px"><h4>WHAT WE DO</h4><ul><li>Web Design</li><li>Social Media Management</li><li>SEO/PPC Traffic</li><li>Display</li><li>Mobile Apps</li><li>On &amp; Offline Marketing Services</li></ul></div>
  <div class="f-col abs" style="left:493px"><h4>FOLLOW</h4><ul><li class="soc"><i></i>Circlet</li><li class="soc"><i></i>Chirper</li><li class="soc"><i style="background:#d9452f"></i>Plusroom</li><li class="soc"><i></i>Linkwell</li></ul></div>

  <div class="quick">
    <h4 class="abs">QUICK CONTACT</h4>
    <div class="field abs" style="left:685px;top:84px;width:224px;height:32px">Name*</div>
    <div class="field abs" style="left:921px;top:84px;width:224px;height:32px">Email*</div>
    <div class="field abs" style="left:685px;top:128px;width:224px;height:32px">Phone*</div>
    <div class="field abs" style="left:921px;top:128px;width:224px;height:32px;display:flex;justify-content:space-between">Interested in<span style="color:#333">&#9662;</span></div>
    <div class="field abs" style="left:685px;top:172px;width:387px;height:70px">comments</div>
    <div class="btn-send abs">SEND</div>
    <p class="req-note abs">* denotes required field</p>
  </div>

  <div class="footer-base abs"><span>Privacy Policy &nbsp;/ &nbsp;Terms of Service &nbsp;/ &nbsp;Sitemap</span><span>&copy;2013 Brindle Marketing. All Rights Reserved</span></div>
</footer>

</body>
</html>
```